Postcard Design Project

We are a small printing company specializing in envelope printing.
We market to churches and medical offices.

Industry/Entity Type

It Company

```html
<!DOCTYPE html>
<html lang="en">
<head>
<meta charset="utf-8">
<title>Corvell Press – Envelope Postcard</title>
<link href="https://fonts.googleapis.com/css2?family=Oswald:wght@500;600;700&display=swap" rel="stylesheet">
<style>
  :root {
    --bg: #e9f1f8;
    --red: #981b1e;
    --red-dark: #8a1a1c;
    --yellow: #ffec00;
    --burst: #fff200;
    --burst-red: #e31e24;
    --white: #ffffff;
    --ink: #111111;
  }
  * { margin: 0; padding: 0; box-sizing: border-box; }
  html, body { width: 1200px; height: 816px; overflow: hidden; background: var(--bg); }
  .postcard {
    position: relative;
    width: 1200px;
    height: 816px;
    overflow: hidden;
    background: var(--bg);
    font-family: "Oswald", "Arial Narrow", sans-serif;
  }
  .shapes { position: absolute; inset: 0; }
  .headline {
    position: absolute;
    left: 52px;
    top: 40px;
    color: var(--white);
    text-transform: uppercase;
    font-weight: 700;
    line-height: 1;
    text-shadow: 3px 3px 0 var(--ink);
  }
  .headline__lead { font-size: 70px; letter-spacing: 0.5px; display: block; margin-bottom: 8px; }
  .headline__rest { font-size: 47px; display: block; line-height: 1.02; }
  .brand {
    position: absolute;
    left: 852px;
    top: 52px;
    width: 220px;
    text-align: center;
    color: var(--red);
    font-weight: 700;
    font-size: 46px;
    line-height: 1.05;
    text-transform: uppercase;
  }
  .tagline {
    position: absolute;
    left: 758px;
    top: 184px;
    color: var(--yellow);
    font-weight: 600;
    font-size: 38px;
    line-height: 1.08;
    text-transform: uppercase;
  }
  .tagline span { display: block; }
  .tagline span:first-child { padding-left: 14px; }
  .burst-text {
    position: absolute;
    left: 560px;
    top: 255px;
    width: 150px;
    text-align: center;
    color: var(--burst-red);
    font-weight: 700;
    line-height: 0.95;
    transform: rotate(-20deg);
    text-transform: uppercase;
  }
  .burst-text__big { display: block; font-size: 58px; }
  .burst-text__small { display: block; font-size: 36px; }
  .services { list-style: none; position: absolute; left: 0; top: 0; }
  .services li {
    position: absolute;
    white-space: nowrap;
    color: var(--red-dark);
    font-weight: 500;
    font-size: 35px;
    line-height: 1;
  }
  .offer {
    position: absolute;
    left: 543px;
    top: 712px;
    color: var(--yellow);
    font-weight: 600;
    font-size: 47px;
    line-height: 1.2;
  }
</style>
</head>
<body>
<main class="postcard">
  <svg class="shapes" width="1200" height="816" viewBox="0 0 1200 816">
    <defs>
      <linearGradient id="header-fade" x1="0" y1="0" x2="1" y2="0">
        <stop offset="0" stop-color="#f4ece8"/>
        <stop offset="0.35" stop-color="#c6786a"/>
        <stop offset="1" stop-color="#9c2b26"/>
      </linearGradient>
      <linearGradient id="photo-tones" x1="0" y1="0" x2="1" y2="1">
        <stop offset="0" stop-color="#d9b08c"/>
        <stop offset="0.5" stop-color="#b0582f"/>
        <stop offset="1" stop-color="#5f3a2a"/>
      </linearGradient>
      <linearGradient id="envelope-tones" x1="0" y1="0" x2="1" y2="0">
        <stop offset="0" stop-color="#efe6c4"/>
        <stop offset="0.6" stop-color="#1f8a3e"/>
        <stop offset="1" stop-color="#c7ccd0"/>
      </linearGradient>
    </defs>

    <polygon class="header-band" points="0,0 752,0 696,248 0,248" fill="url(#header-fade)"/>
    <polygon class="tagline-band" points="688,180 1200,180 1200,277 658,277" fill="var(--red)"/>

    <rect class="photo-area" x="0" y="240" width="520" height="576" fill="url(#photo-tones)" role="img" aria-label="Photo of two women opening an envelope together"/>
    <polygon class="divider-stripe" points="612,416 622,416 490,816 476,816" fill="var(--red)"/>

    <rect class="envelopes-art" x="750" y="300" width="306" height="160" rx="4" fill="url(#envelope-tones)" role="img" aria-label="Illustration of cream, green and grey envelopes"/>

    <g class="burst">
      <polygon transform="translate(638,328)" fill="#333" opacity="0.55"
        points="0,-100 12,-79 31,-95 36,-71 59,-81 56,-57 81,-59 71,-36 95,-31 79,-12 100,0 79,12 95,31 71,36 81,59 56,57 59,81 36,71 31,95 12,79 0,100 -12,79 -31,95 -36,71 -59,81 -56,57 -81,59 -71,36 -95,31 -79,12 -100,0 -79,-12 -95,-31 -71,-36 -81,-59 -56,-57 -59,-81 -36,-71 -31,-95 -12,-79"/>
      <polygon transform="translate(632,322)" fill="var(--burst)"
        points="0,-100 12,-79 31,-95 36,-71 59,-81 56,-57 81,-59 71,-36 95,-31 79,-12 100,0 79,12 95,31 71,36 81,59 56,57 59,81 36,71 31,95 12,79 0,100 -12,79 -31,95 -36,71 -59,81 -56,57 -81,59 -71,36 -95,31 -79,12 -100,0 -79,-12 -95,-31 -71,-36 -81,-59 -56,-57 -59,-81 -36,-71 -31,-95 -12,-79"/>
    </g>

    <g class="bullet-marks" fill="var(--red)">
      <polygon points="586,492 624,492 619,508 581,508"/>
      <polygon points="573,532 611,532 606,548 568,548"/>
      <polygon points="560,572 598,572 593,588 555,588"/>
      <polygon points="547,612 585,612 580,628 542,628"/>
      <polygon points="534,652 572,652 567,668 529,668"/>
    </g>

    <polygon class="offer-band" points="512,702 1200,702 1200,792 482,792" fill="var(--red)"/>
  </svg>

  <h1 class="headline">
    <span class="headline__lead">What do you do</span>
    <span class="headline__rest">When you're down to your</span>
    <span class="headline__rest">last box of envelopes?</span>
  </h1>

  <div class="brand">Corvell Press</div>

  <p class="tagline">
    <span>For fast, economical,</span>
    <span>quality envelopes.</span>
  </p>

  <p class="burst-text">
    <span class="burst-text__big">No</span>
    <span class="burst-text__small">Problem</span>
  </p>

  <ul class="services">
    <li style="left:645px; top:480px;">Custom Business Envelopes</li>
    <li style="left:632px; top:520px;">Free Copy Changes</li>
    <li style="left:619px; top:560px;">Church Offering Envelopes</li>
    <li style="left:606px; top:600px;">Medical Billing Envelopes</li>
    <li style="left:593px; top:640px;">Free Shipping</li>
  </ul>

  <p class="offer">Variety of Paper and Size Available</p>
</main>
</body>
</html>
```